Banner Ad for 2nd opinion radiology

I have a service to provide expert second opinions from US trained radiologist for people's CT/MRI studies, worldwide.
The ad should be simple and catchy, with a black background, as most radiology studies are black. It can have a line drawing/cartoon of a CT or MRI or xray. It should have the website name: scanvell.co
The ad should convey a simple process, expert second opinions, and worldwide audience.
Updates
Here is an idea: Using the words in lower case across the banner:
"scanvell" In the location of the "a" will the the shape of a skull or preferably sagittal brain mri. YOu can google sagittal brain mri to get an idea of what it looks like. Then for the "t" put a faucet coming of the tail of the 't'. This can all be line art...
Looking forward to the designs!
Reason: Need more creative designs. Designs need to be catchy/striking with line art.
Target Market(s)
Target: upper class China, India, Pak, Mid East
Industry/Entity Type
Mri
Look and feel

```html
<!DOCTYPE html>
<html lang="en">
<head>
<meta charset="utf-8">
<title>scanvell.co — expert second opinion reports banner</title>
<link rel="stylesheet" href="https://fonts.googleapis.com/css2?family=Montserrat:wght@300;400;600;700&family=Handlee&display=swap">
<style>
  :root {
    --page: #e6e6e6;
    --banner: #050505;
    --white: #ffffff;
    --blue: #1f5fae;
    --scan-deep: #02101d;
    --scan-mid: #0b3c6e;
    --scan-glow: #3aa6e6;
  }
  * { margin: 0; padding: 0; box-sizing: border-box; }
  html, body {
    width: 1200px; height: 1000px; overflow: hidden;
    background: var(--page);
  }
  .canvas { position: relative; width: 1200px; height: 1000px; }
  .banner {
    position: absolute; left: 57px; top: 357px;
    width: 1086px; height: 288px;
    background: var(--banner);
    overflow: hidden;
    font-family: "Montserrat", sans-serif;
    color: var(--white);
  }
  .site {
    position: absolute; left: 48px; top: 31px;
    font-size: 14px; font-weight: 400; letter-spacing: 0.3px;
  }
  .modality { position: absolute; left: 46px; line-height: 1; white-space: nowrap; }
  .modality--mri { top: 44px; font-size: 80px; font-weight: 700; color: var(--blue); letter-spacing: -1px; }
  .modality--ct { top: 116px; font-size: 64px; font-weight: 300; color: var(--blue); letter-spacing: 30px; }
  .modality--xray { top: 182px; font-size: 36px; font-weight: 700; letter-spacing: 6px; }
  .reports {
    position: absolute; left: 240px; top: 186px;
    font-family: "Handlee", cursive; font-size: 25px;
    color: var(--blue); letter-spacing: 9.5px;
  }
  .reports-arrow { position: absolute; left: 390px; top: 180px; }
  .terms {
    position: absolute; left: 476px; top: 30px;
    list-style: none;
  }
  .term {
    display: flex; align-items: center; line-height: 1;
    height: 28px; white-space: nowrap;
  }
  .term::before {
    content: ""; width: 13px; height: 16px; margin-right: 6px;
    background: var(--white); flex: none;
  }
  .term--bold { font-weight: 700; font-size: 29px; letter-spacing: 5px; }
  .term--bold-small { font-weight: 700; font-size: 22px; letter-spacing: 2.5px; }
  .term--light { font-weight: 400; font-size: 26px; letter-spacing: 3.5px; }
  .term--thin-blue { font-weight: 300; font-size: 21px; letter-spacing: 3.5px; color: var(--blue); }
  .term--blue { font-weight: 700; font-size: 33px; letter-spacing: 4px; color: var(--blue); }
  .glossary {
    position: absolute; left: 16px; top: 246px;
    font-family: "Handlee", cursive; font-size: 19px;
    white-space: nowrap; letter-spacing: 1.6px;
  }
  .scan-panel { position: absolute; left: 0; top: 0; }
</style>
</head>
<body>
<main class="canvas">
  <section class="banner">
    <p class="site">www.scanvell.co</p>
    <p class="modality modality--mri">MRI</p>
    <p class="modality modality--ct">CTI</p>
    <p class="modality modality--xray">X-RAY</p>

    <p class="reports">reports</p>
    <svg class="reports-arrow" width="52" height="44" viewBox="0 0 52 44" aria-hidden="true">
      <path d="M6 16 C14 4 40 2 44 14 C48 26 30 36 14 34" fill="none" stroke="var(--white)" stroke-width="2.5" stroke-linecap="round"/>
      <path d="M20 26 L12 34 L22 40" fill="none" stroke="var(--white)" stroke-width="2.5" stroke-linecap="round" stroke-linejoin="round"/>
    </svg>

    <ul class="terms">
      <li class="term term--bold">expert</li>
      <li class="term term--thin-blue">SECOND OPINIONS</li>
      <li class="term term--light">US TRAINED</li>
      <li class="term term--light">WORLDWIDE</li>
      <li class="term term--bold-small">simple process</li>
      <li class="term term--blue">fractures</li>
      <li class="term term--blue">sclerosis</li>
    </ul>

    <p class="glossary">Coronal •Axial •Sagittal • Sequence • Enhancing • MRA • Hyperintensity • Artifact</p>

    <svg class="scan-panel" width="1086" height="288" viewBox="0 0 1086 288">
      <defs>
        <radialGradient id="scanTone" cx="0.45" cy="0.5" r="0.6">
          <stop offset="0" stop-color="var(--scan-glow)"/>
          <stop offset="0.45" stop-color="var(--scan-mid)"/>
          <stop offset="1" stop-color="var(--scan-deep)"/>
        </radialGradient>
      </defs>
      <path d="M790 0 Q 822 144 792 288 L 1086 288 L 1086 0 Z" fill="url(#scanTone)" role="img" aria-label="Blue-toned axial MRI scan of a brain"/>
      <path d="M790 0 Q 822 144 792 288" fill="none" stroke="var(--white)" stroke-width="3"/>
    </svg>
  </section>
</main>
</body>
</html>
```